KLT-AZ Presentation Folder

The old design is attached. We're looking to revamp our Arizona offices with a fresh new look.

Front Cover

The Company Logo is prominently displayed.
Tagline: "Improving Homes. Improving Lives."
Image of a beautiful home showcasing new windows and doors
Website: crestfieldpaneworksaz.example
Social media icons: Chatterloop, Snapvale, ClipDrome, Rateburrow
Mention: "Follow us for the latest updates and tips."

Back Cover

Thank You Message: "Thank you for choosing Crestfield Pane Works. We appreciate your trust in us to improve your home."
Contact Information:
Customer Service: 480.555.0187
Call Center: 480.555.0143
ROC License Number: #418302
Additional social media handles and website details.
Small disclaimer or legal note if necessary.

Inside Left Panel

Photo of Doug and Marian Solvik (founders)
Short blurb/quote: “Our mission is to provide the best window and door solutions with a personal touch. Thank you for letting us be a part of your home improvement journey.”
Slots for business cards (either sales or customer service rep)

Inside Right Panel

Thank You Message: “We’re honored to be a part of your home transformation. Our commitment to quality and customer satisfaction ensures you receive the best service and products.”
List of Services (e.g., window and door installations, energy-efficient solutions)
Highlight the company’s QTC accreditation A+

Encourage the customer to reach out if they need further assistance or have any questions, with a reminder of the contact details.

https://www.qtcreview.example/us/az/gilbert/profile/home-improvement/crestfield-pane-works-4471-2000058314

https://crestfieldpaneworksaz.example/

We need thirty more days to decide.

Gathering more feedback

Designs look the same

```html
<!DOCTYPE html>
<html lang="en">
<head>
<meta charset="utf-8">
<title>Crestfield Pane Works – Presentation Folder Inside</title>
<link href="https://fonts.googleapis.com/css2?family=Tinos:ital,wght@0,400;0,700;1,400&display=swap" rel="stylesheet">
<style>
  :root {
    --navy: #003a70;
    --navy-deep: #00264d;
    --stripe: rgba(255,255,255,0.06);
    --sky: #7cc6d8;
    --lime: #8dc63f;
    --white: #ffffff;
    --stage: #e6e7ea;
    --fold-shade: rgba(0,0,0,0.16);
  }
  * { box-sizing: border-box; margin: 0; padding: 0; }
  html, body { width: 1200px; height: 991px; overflow: hidden; background: var(--stage); }
  body { position: relative; font-family: 'Tinos', 'Times New Roman', serif; }

  .folder {
    position: absolute; left: 30px; top: 115.5px;
    width: 1800px; height: 1200px;
    transform: scale(0.63333); transform-origin: 0 0;
    background: var(--white);
    box-shadow: 0 12px 40px rgba(0,0,0,0.25);
    overflow: hidden;
  }
  .fold-shade-left, .fold-shade-right {
    position: absolute; top: 0; height: 1200px; width: 120px;
  }
  .fold-shade-left { left: 780px; background: linear-gradient(to right, rgba(0,0,0,0), var(--fold-shade)); }
  .fold-shade-right { left: 900px; width: 100px; background: linear-gradient(to right, var(--fold-shade), rgba(0,0,0,0)); }
  .fold-line { position: absolute; left: 899px; top: 0; width: 2px; height: 1200px; background: rgba(0,0,0,0.12); }
  .pocket-shadow { position: absolute; left: 0; top: 730px; width: 1800px; height: 80px;
    background: linear-gradient(to bottom, rgba(0,0,0,0), rgba(0,0,0,0.10)); }

  .pockets { position: absolute; left: 0; top: 0; width: 1800px; height: 1200px; }

  .mission {
    position: absolute; left: 40px; top: 822px;
    color: var(--white); font-style: italic; font-size: 19px; line-height: 21px;
  }
  .founder-bar {
    position: absolute; left: 0; top: 884px; width: 340px; height: 60px;
    background: linear-gradient(to right, var(--navy-deep) 60%, rgba(0,38,77,0));
    padding: 10px 0 0 40px;
  }
  .founder-name { color: var(--sky); font-weight: 700; font-size: 22px; line-height: 24px; }
  .founder-role { color: var(--white); font-size: 16px; line-height: 18px; }

  .founder-photo {
    position: absolute; left: 0; top: 953px; width: 324px; height: 208px;
    background: linear-gradient(135deg, #c9b23a 0%, #9aa63c 35%, #d7cfc2 70%, #eae6df 100%);
    border-top-right-radius: 90px 70px;
    box-shadow: 10px 5px 0 var(--lime);
  }

  .card-slot {
    position: absolute; left: 453px; top: 960px; width: 350px; height: 199px;
    border: 1.5px solid rgba(255,255,255,0.55);
  }

  .honored {
    position: absolute; left: 1019px; top: 842px; width: 760px;
    color: var(--sky); font-style: italic; font-size: 22px; line-height: 25px;
  }
  .brand-box {
    position: absolute; left: 932px; top: 920px; width: 220px; height: 112px;
    background: var(--white); border-radius: 0 30px 30px 0;
    display: flex; align-items: center; gap: 10px; padding-left: 40px;
  }
  .brand-mark { width: 22px; height: 22px; background: var(--navy); flex: none; }
  .brand-name { color: var(--navy); font-size: 19px; line-height: 19px; font-weight: 400; }

  .contact { position: absolute; color: var(--white); font-weight: 700; }
  .contact-label { font-size: 19px; line-height: 20px; }
  .contact-number { font-size: 35px; line-height: 38px; }
  .contact-service { left: 977px; top: 1050px; }
  .contact-center { left: 969px; top: 1130px; }
  .contact-rule { position: absolute; left: 974px; top: 1114px; width: 197px; height: 1.5px; background: rgba(255,255,255,0.7); }

  .service { position: absolute; top: 950px; font-weight: 700; font-size: 25px; line-height: 25px; letter-spacing: 0.5px; }
  .service-install { left: 1287px; color: var(--sky); }
  .service-energy { left: 1546px; color: var(--lime); }
  .service-divider { position: absolute; left: 1506px; top: 942px; width: 1.5px; height: 70px; background: rgba(255,255,255,0.6); }

  .accreditation { position: absolute; left: 1287px; top: 1063px; width: 144px; height: 56px; background: var(--white); border-radius: 6px; }
  .rating {
    position: absolute; left: 1439px; top: 1063px; width: 68px; height: 56px;
    background: var(--white); border-radius: 6px; color: var(--navy);
    font-family: Arial, Helvetica, sans-serif; font-size: 34px; line-height: 56px; text-align: center;
  }
  .social { position: absolute; left: 1525px; top: 1077px; display: flex; align-items: center; color: var(--white); font-size: 11px; }
  .social span { padding: 0 7px; border-right: 1.5px solid rgba(255,255,255,0.6); line-height: 28px; }
  .social span:last-child { border-right: none; }
  .follow { position: absolute; left: 1533px; top: 1110px; color: var(--white); font-size: 10.5px; letter-spacing: 1.5px; }

  .web-bar { position: absolute; left: 1259px; top: 1138px; width: 541px; height: 62px; }
  .web-address {
    position: absolute; left: 1280px; top: 1150px; width: 500px; text-align: center;
    color: var(--navy); font-weight: 700; font-size: 28px; line-height: 36px;
  }
</style>
</head>
<body>
  <div class="folder">
    <div class="pocket-shadow"></div>
    <div class="fold-shade-left"></div>
    <div class="fold-shade-right"></div>
    <div class="fold-line"></div>

    <svg class="pockets" viewBox="0 0 1800 1200" width="1800" height="1200" aria-hidden="true">
      <defs>
        <pattern id="band-lines" width="10" height="10" patternUnits="userSpaceOnUse">
          <rect width="10" height="5" fill="rgba(255,255,255,0.06)"/>
        </pattern>
      </defs>
      <path d="M0 802 H769 Q854 802 854 887 L884 1200 H0 Z" fill="#003a70"/>
      <path d="M500 930 H864 L884 1200 H500 Z" fill="url(#band-lines)"/>
      <path d="M1039 802 H1800 V1200 H914 L946 897 Q946 802 1039 802 Z" fill="#003a70"/>
      <path d="M930 930 H1800 V1200 H914 Z" fill="url(#band-lines)"/>
      <path class="web-bar-shape" d="M1275 1138 H1800 V1200 H1259 L1265 1150 Q1266 1138 1275 1138 Z" fill="#8dc63f"/>
    </svg>

    <section class="panel-left">
      <p class="mission">Our mission is to provide the best window and door solutions with a personal touch.<br>Thank you for letting us be a part of your home improvement journey.</p>
      <div class="founder-bar">
        <p class="founder-name">Doug and Marian Solvik</p>
        <p class="founder-role">Founders</p>
      </div>
      <div class="founder-photo" role="img" aria-label="Portrait photo of founders Doug and Marian Solvik outdoors"></div>
      <div class="card-slot" aria-label="Business card slot"></div>
    </section>

    <section class="panel-right">
      <p class="honored">We’re honored to be a part of your home transformation. Our commitment to quality and customer satisfaction ensures you receive the best service and products.</p>
      <div class="brand-box">
        <span class="brand-mark"></span>
        <span class="brand-name">Crestfield<br>Pane Works</span>
      </div>

      <div class="contact contact-service">
        <p class="contact-label">Customer Service</p>
        <p class="contact-number">480.555.0187</p>
      </div>
      <div class="contact-rule"></div>
      <div class="contact contact-center">
        <p class="contact-label">Call Center</p>
        <p class="contact-number">480.555.0143</p>
      </div>

      <p class="service service-install">Window &amp; Door<br>Installation</p>
      <div class="service-divider"></div>
      <p class="service service-energy">Energy-Efficient<br>Solutions</p>

      <div class="accreditation" role="img" aria-label="QTC accredited business badge"></div>
      <div class="rating">A+</div>
      <div class="social">
        <span>Chatterloop</span><span>ClipDrome</span><span>Snapvale</span><span>Rateburrow</span>
      </div>
      <p class="follow">Follow us for the latest updates and tips.</p>

      <p class="web-address">www.crestfieldpaneworksaz.example</p>
    </section>
  </div>
</body>
</html>
```